Commercial real estate Brokerage logo, letterhead and business card design

Boutique Commercial real Estate Brokerage and development company requires logo, letterhead/stationary and business card design. For reference, competitors include Harper Vale Brightwood, Pemberton & Oakhurst, Renwick Galloway and Tamsin which all have designs which evoke strong corporate image.
Updates

The name of the firm is Brantley Real Estate. If you look at my competitors web sites you will see their logos. I am looking for something that has a similar flavor - not the same colors or graphics - just how you feel when you see their logo. 
1. www.hvb-realty.example
2. http://www.tamsinprop.example/en-us
3. http://www.pembertonoakhurst.example/

Industry/Entity Type

Real Estate

```html
<!DOCTYPE html>
<html lang="en">
<head>
<meta charset="utf-8">
<title>Brantley Real Estate — Stationery</title>
<link rel="stylesheet" href="https://fonts.googleapis.com/css2?family=Jost:wght@400;500&family=Libre+Baskerville&display=swap">
<style>
:root{
  --backdrop:#8c6440;
  --blue:#2e3f9e;
  --ink:#1e1e1e;
  --paper:#ffffff;
  --faint:#e9eaf3;
  --text:#222;
}
*{box-sizing:border-box;margin:0;padding:0}
html,body{width:1200px;height:824px;overflow:hidden}
body{background:var(--backdrop);font-family:"Jost",sans-serif;color:var(--text);position:relative}
.sheet{position:absolute;background:var(--paper);box-shadow:0 2px 6px rgba(0,0,0,.35);overflow:hidden}
.dot{display:inline-block;border-radius:50%;background:var(--blue);flex:none}
.brand{position:absolute;display:flex;align-items:center;gap:10px}
.brand-name{font-weight:500;line-height:1.2;color:var(--ink)}
.contact{position:absolute;font-size:7px;line-height:10px;border-left:1px solid #999;padding-left:4px}
.contact .serif{font-family:"Libre Baskerville",serif;font-size:6px}
.footer-strip{position:absolute;left:0;bottom:0;width:100%;height:12px}
.small{font-size:7px}
.center{text-align:center}
/* letterhead */
.letterhead{left:52px;top:58px;width:332px;height:430px}
.watermark{position:absolute;left:78px;top:142px;width:176px;height:176px;border-radius:50%;background:var(--faint);display:flex;align-items:center;justify-content:center;color:#d6d8e8;font-weight:500;font-size:22px;text-align:center;line-height:1.2}
.letterhead .address{position:absolute;left:0;width:100%;top:406px;text-align:center}
/* fax */
.fax{left:428px;top:58px;width:333px;height:430px}
.fax-title{position:absolute;left:18px;top:90px;font-size:22px;font-weight:400}
.fax-field{position:absolute;font-size:8px;border-bottom:1.2px solid var(--ink);height:18px;padding-top:2px}
.fax-footer{position:absolute;top:405px;left:0;width:100%;display:flex;justify-content:center;gap:10px}
/* envelopes */
.envelope{left:776px;width:372px;height:160px}
.env-flap{position:absolute;left:0;top:0;width:100%;height:57px;border-bottom:1px solid #555;display:flex;align-items:center;justify-content:center}
.env-flap.blue{background:var(--blue);border:0}
.env-flap.black{background:var(--ink);border:0}
.env-flap .label{font-weight:500;font-size:12px;color:var(--blue);display:flex;align-items:center;gap:6px}
.env-flap.blue .label,.env-flap.black .label{color:#fff}
.env-flap.blue .dot,.env-flap.black .dot{background:#fff}
.dl{left:771px;top:603px;width:372px;height:160px}
/* cards */
.card{width:206px;height:117px}
.card.blue{background:var(--blue);color:#fff}
.card.black{background:var(--ink);color:#fff}
.card-web{position:absolute;left:0;width:100%;bottom:10px;text-align:center;font-size:7.5px;letter-spacing:.5px}
.card-web.serif{font-family:"Libre Baskerville",serif;font-size:7px}
.big-brand{position:absolute;left:0;top:18px;width:100%;text-align:center;font-weight:500;font-size:21px;line-height:1.35}
.emblem{position:absolute;left:50%;top:10px;transform:translateX(-50%);width:82px;height:82px;border-radius:50%;display:flex;align-items:center;justify-content:center;text-align:center;font-weight:500;font-size:11px;line-height:1.2}
</style>
</head>
<body>

<!-- Letterhead -->
<section class="sheet letterhead">
  <div class="brand" style="left:18px;top:14px">
    <span class="dot" style="width:44px;height:44px"></span>
    <span class="brand-name" style="font-size:14px">Brantley<br>Real Estate</span>
  </div>
  <div class="contact" style="left:222px;top:21px">
    ✆ +123 456 7890<br><span class="serif">✉ info@brantleyrealestate.example</span><br>◍ www.brantleyrealestate.example
  </div>
  <div class="watermark">Brantley<br>Real Estate</div>
  <p class="address small">00, Complex name, City name, Zip code 004203</p>
  <svg class="footer-strip" viewBox="0 0 332 12" preserveAspectRatio="none"><polygon points="0,0 162,0 154,12 0,12" fill="var(--ink)"/><polygon points="166,0 332,0 332,12 158,12" fill="var(--blue)"/></svg>
</section>

<!-- Fax -->
<section class="sheet fax">
  <div class="brand" style="left:18px;top:14px">
    <span class="dot" style="width:44px;height:44px"></span>
    <span class="brand-name" style="font-size:14px">Brantley<br>Real Estate</span>
  </div>
  <div class="contact" style="left:258px;top:24px">00, Complex name<br>City name<br>Zip code 004203</div>
  <h1 class="fax-title">FAX</h1>
  <div class="fax-field" style="left:21px;top:134px;width:176px">To</div>
  <div class="fax-field" style="left:200px;top:134px;width:98px">From</div>
  <div class="fax-field" style="left:21px;top:173px;width:176px">Fax</div>
  <div class="fax-field" style="left:200px;top:173px;width:98px">Pages</div>
  <div class="fax-field" style="left:21px;top:212px;width:176px">Phone</div>
  <div class="fax-field" style="left:200px;top:212px;width:98px">Date</div>
  <div class="fax-field" style="left:21px;top:251px;width:176px">Re</div>
  <div class="fax-field" style="left:200px;top:251px;width:98px">CC</div>
  <div class="fax-footer small">
    <span>✆ +123 456 7890</span><span style="font-family:'Libre Baskerville',serif;font-size:6px">✉ info@brantleyrealestate.example</span><span>◍ www.brantleyrealestate.example</span>
  </div>
  <svg class="footer-strip" viewBox="0 0 333 12" preserveAspectRatio="none"><polygon points="0,0 162,0 154,12 0,12" fill="var(--ink)"/><polygon points="166,0 333,0 333,12 158,12" fill="var(--blue)"/></svg>
</section>

<!-- Envelopes -->
<section class="sheet envelope" style="top:56px">
  <div class="env-flap"><span class="label"><span class="dot" style="width:20px;height:20px"></span>Brantley</span></div>
</section>
<section class="sheet envelope" style="top:237px">
  <div class="env-flap blue"><span class="label"><span class="dot" style="width:20px;height:20px"></span>Brantley</span></div>
</section>
<section class="sheet envelope" style="top:413px">
  <div class="env-flap black"><span class="label"><span class="dot" style="width:20px;height:20px"></span>Brantley</span></div>
</section>

<!-- DL envelope -->
<section class="sheet dl">
  <div class="brand" style="left:14px;top:12px">
    <span class="dot" style="width:44px;height:44px"></span>
    <span class="brand-name" style="font-size:14px">Brantley<br>Real Estate</span>
  </div>
  <p class="small" style="position:absolute;left:16px;top:68px">00, Complex name, City name Zip code 004203</p>
  <div class="dot" style="position:absolute;left:294px;top:72px;width:66px;height:66px;background:var(--faint)"></div>
  <svg class="footer-strip" viewBox="0 0 372 12" preserveAspectRatio="none"><polygon points="0,0 176,0 170,12 0,12" fill="var(--ink)"/><polygon points="182,0 372,0 372,12 176,12" fill="var(--blue)"/></svg>
</section>

<!-- Business cards: front / back variants -->
<section class="sheet card" style="left:54px;top:515px;height:116px">
  <div class="brand" style="left:40px;top:10px">
    <span class="dot" style="width:44px;height:44px"></span>
    <span class="brand-name" style="font-size:13px">Brantley<br>Real Estate</span>
  </div>
  <div style="position:absolute;right:108px;top:68px;text-align:right;font-size:6px;line-height:7.5px">
    <strong style="color:var(--blue);font-size:8px;font-weight:500">Your Name</strong><br>Title<br>00, Complex name<br>City name Zip code 004203
  </div>
  <div class="contact" style="left:103px;top:68px;font-size:5.5px;line-height:11px">
    ✆ +123 456 7890<br><span class="serif" style="font-size:5px">✉ info@brantleyrealestate.example</span><br>◍ www.brantleyrealestate.example
  </div>
  <svg class="footer-strip" style="height:6px" viewBox="0 0 206 6" preserveAspectRatio="none"><polygon points="0,0 98,0 94,6 0,6" fill="var(--ink)"/><polygon points="102,0 206,0 206,6 98,6" fill="var(--blue)"/></svg>
</section>

<section class="sheet card blue" style="left:285px;top:515px;width:205px;height:116px">
  <div class="big-brand">Brantley<br>Real Estate</div>
  <p class="card-web serif">WWW.BRANTLEYREALESTATE.EXAMPLE</p>
</section>

<section class="sheet card black" style="left:508px;top:515px;width:205px;height:116px">
  <div class="brand" style="left:30px;top:14px">
    <span class="dot" style="width:64px;height:64px;background:#fff"></span>
    <span class="brand-name" style="font-size:13px;color:#fff">Brantley<br>Real Estate</span>
  </div>
  <p class="card-web serif">WWW.BRANTLEYREALESTATE.EXAMPLE</p>
</section>

<section class="sheet card blue" style="left:55px;top:650px">
  <div class="emblem" style="background:rgba(255,255,255,.25);color:rgba(255,255,255,.55)">Brantley</div>
  <p class="card-web">www.brantleyrealestate.example</p>
</section>

<section class="sheet card" style="left:285px;top:650px;width:205px;border:1px solid #888">
  <div class="emblem" style="background:var(--blue);color:#fff">Brantley</div>
  <p class="card-web">www.brantleyrealestate.example</p>
</section>

<section class="sheet card blue" style="left:511px;top:650px;width:205px">
  <div class="emblem" style="background:#fff;color:var(--blue)">Brantley</div>
  <p class="card-web">www.brantleyrealestate.example</p>
</section>

</body>
</html>
```